Visit card

Industry/Entity Type

Health Care

Contact Information for Business Card

O VITALE SYSTEMES
Odile Ferrandi - chef de Projet

Requirements
Must have
• 318 Hector Delaunay Street 58210 BÉTHUNE Tel: 33 (0) 387 419 264 Mobile: 06 42 93 17 58 Web: www.vobelasystems.example Contact: o.ferrandi@o-vitalesystemes.example
Should not have
• Respect for color

```html
<!DOCTYPE html>
<html lang="fr">
<head>
<meta charset="utf-8">
<title>O Vitale Systemes – carte de visite</title>
<link href="https://fonts.googleapis.com/css2?family=Lato:wght@400;700;900&display=swap" rel="stylesheet">
<style>
  :root {
    --card-dark: #3e3e40;
    --card-white: #ffffff;
    --brand-red: #e21f2b;
    --text-dark: #3a3a3c;
    --text-light: #ffffff;
    --stage: #d9d9db;
  }
  * { margin: 0; padding: 0; box-sizing: border-box; }
  html, body { width: 1200px; height: 900px; overflow: hidden; }
  body {
    background: var(--stage);
    font-family: "Lato", Arial, sans-serif;
    position: relative;
  }
  .card {
    position: absolute;
    width: 700px;
    height: 400px;
    overflow: hidden;
    box-shadow: 0 8px 24px rgba(0,0,0,.25);
  }
  /* back side */
  .card-back {
    left: 430px; top: 50px;
    background: var(--card-dark);
    display: flex; align-items: center; justify-content: center; gap: 22px;
  }
  .brand-dot {
    width: 84px; height: 84px; border-radius: 50%;
    border: 12px solid var(--card-white);
  }
  .brand-name {
    font-weight: 900; color: var(--brand-red);
    font-size: 46px; line-height: 1; letter-spacing: 1px;
  }
  /* front side */
  .card-front { left: 70px; top: 450px; background: var(--card-white); }
  .card-front .wave { position: absolute; inset: 0; }
  .identity { position: absolute; left: 40px; top: 34px; }
  .identity .brand-name { font-size: 38px; }
  .person-name {
    margin-top: 26px; color: var(--brand-red);
    font-weight: 700; font-size: 24px; text-transform: uppercase;
  }
  .person-role, .address {
    color: var(--text-dark); font-size: 16px; line-height: 1.35;
  }
  .person-role { margin-bottom: 6px; }
  .contacts {
    position: absolute; right: 26px; bottom: 20px;
    list-style: none; color: var(--text-light);
    font-size: 17px; line-height: 1.4; text-align: right;
  }
  .contacts li { display: flex; justify-content: flex-end; align-items: center; gap: 10px; }
  .contacts svg { width: 14px; height: 14px; flex: none; }
</style>
</head>
<body>

<section class="card card-back" aria-label="Verso de la carte">
  <span class="brand-dot"></span>
  <span class="brand-name">O VITALE SYSTEMES</span>
</section>

<section class="card card-front" aria-label="Recto de la carte">
  <svg class="wave" viewBox="0 0 700 400" width="700" height="400">
    <path d="M0,200 C60,270 200,272 380,258 C470,250 540,215 700,140" fill="none" stroke="var(--brand-red)" stroke-width="9"/>
    <path d="M0,220 C60,285 200,286 380,274 C470,266 540,233 700,162 L700,400 L0,400 Z" fill="var(--card-dark)"/>
    <path d="M0,220 C60,285 200,286 380,274 C470,266 540,233 700,162" fill="none" stroke="var(--card-white)" stroke-width="4"/>
    <circle cx="570" cy="180" r="66" fill="var(--card-dark)" stroke="var(--card-white)" stroke-width="7"/>
  </svg>

  <div class="identity">
    <div class="brand-name">O VITALE SYSTEMES</div>
    <div class="person-name">Odile Ferrandi</div>
    <div class="person-role">Chef de Projet</div>
    <div class="address">318 Rue Hector Delaunay<br>58210 BÉTHUNE</div>
  </div>

  <ul class="contacts">
    <li>+33 (0) 387 419 264
      <svg viewBox="0 0 14 14"><path d="M3,1 L5,1 L6,4 L4.5,5.5 C5.5,7.5 6.5,8.5 8.5,9.5 L10,8 L13,9 L13,11 C13,12 12,13 11,13 C6,13 1,8 1,3 C1,2 2,1 3,1Z" fill="var(--brand-red)"/></svg></li>
    <li>06 42 93 17 58
      <svg viewBox="0 0 14 14"><rect x="3.5" y="1" width="7" height="12" rx="1.2" fill="none" stroke="var(--brand-red)" stroke-width="1.4"/></svg></li>
    <li>www.vobelasystems.example
      <svg viewBox="0 0 14 14"><g fill="none" stroke="var(--brand-red)" stroke-width="1.2"><circle cx="7" cy="7" r="6"/><ellipse cx="7" cy="7" rx="2.6" ry="6"/><line x1="1" y1="7" x2="13" y2="7"/></g></svg></li>
    <li>o.ferrandi@o-vitalesystemes.example
      <svg viewBox="0 0 14 14"><g fill="none" stroke="var(--brand-red)" stroke-width="1.3"><rect x="1" y="3" width="12" height="8"/><path d="M1,3 L7,8 L13,3"/></g></svg></li>
  </ul>
</section>

</body>
</html>
```